KVZ Anchorworks Needs a Packing Design

We need a packing design for products, for example bolts, screws etc.
The accepted design shall be printed in box or cartons made of paper.
We would like to see design that is remarkable and not colourful.
Attached our products photo.

```html
<!DOCTYPE html>
<html lang="en">
<head>
<meta charset="utf-8">
<title>KVZ Anchorworks – Carton Dieline</title>
<link rel="stylesheet" href="https://fonts.googleapis.com/css2?family=Archivo:wght@400;600;800&display=swap">
<style>
  :root {
    --cardboard: #bda57f;
    --print-black: #000000;
    --print-red: #da2a2a;
    --fold-line: #3a3a3a;
    --ink: #111111;
    --page: #ffffff;
  }
  * { margin: 0; padding: 0; box-sizing: border-box; }
  html, body { width: 1200px; height: 1000px; overflow: hidden; background: var(--page); }
  body { position: relative; font-family: "Archivo", Arial, sans-serif; color: var(--ink); }

  .panel { position: absolute; border: 1px solid var(--fold-line); overflow: hidden; }
  .panel--raw { background: var(--cardboard); }
  .panel--black { background: var(--print-black); color: var(--cardboard); }

  .spine { position: absolute; left: 712px; top: 63px; width: 74px; height: 860px; background: var(--print-black); }
  .lid { left: 785px; top: 63px; width: 214px; height: 145px; }
  .side-left { left: 569px; top: 207px; width: 144px; height: 287px; border-right: none; }
  .front { left: 785px; top: 207px; width: 214px; height: 287px; }
  .side-right { left: 998px; top: 207px; width: 144px; height: 287px; }
  .base { left: 785px; top: 493px; width: 214px; height: 144px; }
  .back { left: 785px; top: 636px; width: 214px; height: 287px; }

  .wordmark { position: absolute; left: 0; right: 0; text-align: center; font-weight: 800; line-height: 1; color: var(--print-black); }
  .wordmark__short { display: block; font-size: 34px; letter-spacing: 2px; }
  .wordmark__full { display: block; font-size: 13px; letter-spacing: 2px; margin-top: 4px; }
  .wordmark--small .wordmark__short { font-size: 19px; letter-spacing: 1px; }
  .wordmark--small .wordmark__full { font-size: 8px; letter-spacing: 1.2px; margin-top: 3px; }
  .panel--black .wordmark { color: var(--cardboard); }

  .lid .wordmark { top: 44px; }
  .front .wordmark { top: 64px; }
  .side-left .wordmark, .side-right .wordmark { top: 222px; }

  .rule { position: absolute; left: 39px; width: 136px; height: 2px; background: var(--print-black); }
  .front .rule { top: 190px; }

  .spec { position: absolute; left: 0; right: 0; top: 220px; text-align: center; font-size: 7.5px; font-weight: 600; letter-spacing: 1.1px; line-height: 14px; }

  .side-spec { position: absolute; left: 72px; top: 118px; width: 170px; transform: translate(-50%, -50%) rotate(90deg); text-align: center; font-size: 7.5px; font-weight: 600; letter-spacing: 1.2px; line-height: 14px; white-space: nowrap; }
  .side-right .side-spec { color: var(--print-black); }

  .flipped { position: absolute; inset: 0; transform: rotate(180deg); }
  .base .wordmark { top: 42px; }

  .back__heading { position: absolute; left: 0; right: 0; top: 16px; text-align: center; font-size: 12px; font-weight: 800; letter-spacing: 1.6px; line-height: 15px; }
  .back__copy { position: absolute; left: 20px; right: 20px; top: 62px; font-size: 4.6px; line-height: 8px; letter-spacing: 0.4px; text-align: center; }
  .back__copy p + p { margin-top: 8px; }
  .back .rule { top: 206px; }
  .back__sign { position: absolute; left: 36px; top: 232px; }
  .back__sign .wordmark { position: static; text-align: left; }
  .back__sign .wordmark__short { font-size: 16px; }
  .back__sign .wordmark__full { font-size: 6.5px; }
  .back__address { position: absolute; left: 112px; top: 234px; font-size: 4.6px; line-height: 7px; letter-spacing: 0.3px; }

  .legend { position: absolute; left: 489px; top: 840px; list-style: none; }
  .legend__item { display: flex; align-items: center; height: 30px; margin-bottom: 16px; font-size: 12px; letter-spacing: 0.3px; }
  .legend__swatch { width: 28px; height: 30px; margin-right: 16px; }
  .legend__swatch--raw { background: var(--cardboard); }
  .legend__swatch--black { background: var(--print-black); }
  .legend__swatch--red { background: var(--print-red); }
</style>
</head>
<body>
  <div class="spine"></div>

  <section class="panel panel--raw lid">
    <div class="wordmark"><span class="wordmark__short">KVZ</span><span class="wordmark__full">ANCHORWORKS</span></div>
  </section>

  <section class="panel panel--black side-left">
    <div class="side-spec">Metric hex bolts<br>Chrome plated - Class 8.8 steel<br>10mm x 1.5mm</div>
    <div class="wordmark wordmark--small"><span class="wordmark__short">KVZ</span><span class="wordmark__full">ANCHORWORKS</span></div>
  </section>

  <section class="panel panel--raw front">
    <div class="wordmark"><span class="wordmark__short">KVZ</span><span class="wordmark__full">ANCHORWORKS</span></div>
    <div class="rule"></div>
    <p class="spec">Metric Hex Bolts<br>Chrome Plated - Class 8.8 Steel<br>10mm x 1.5mm</p>
  </section>

  <section class="panel panel--raw side-right">
    <div class="side-spec">Metric hex bolts<br>Chrome plated - Class 8.8 steel<br>10mm x 1.5mm</div>
    <div class="wordmark wordmark--small"><span class="wordmark__short">KVZ</span><span class="wordmark__full">ANCHORWORKS</span></div>
  </section>

  <section class="panel panel--raw base">
    <div class="flipped">
      <div class="wordmark"><span class="wordmark__short">KVZ</span><span class="wordmark__full">ANCHORWORKS</span></div>
    </div>
  </section>

  <section class="panel panel--raw back">
    <div class="flipped">
      <h2 class="back__heading">THE BEST FASTENERS<br>FOR YOUR PROJECT</h2>
      <div class="back__copy">
        <p>Our Promise - Every bolt we pack is checked for thread, finish and strength before it leaves our floor. We stock a wide range of metric and imperial sizes in steel, zinc and chrome, ready for builders, workshops and makers who need parts that fit first time.</p>
        <p>Need help choosing the right fastener? Our team can match size, grade and coating to your job and ship the same day from our local warehouse.</p>
      </div>
      <div class="rule"></div>
      <div class="back__sign">
        <div class="wordmark wordmark--small"><span class="wordmark__short">KVZ</span><span class="wordmark__full">ANCHORWORKS</span></div>
      </div>
      <p class="back__address">KVZ Anchorworks Pty Ltd<br>Unit 4, 18 Harbour Road<br>Riverton VIC 3999<br>www.kvzanchorworks.example</p>
    </div>
  </section>

  <ul class="legend">
    <li class="legend__item"><span class="legend__swatch legend__swatch--raw"></span>RAW CARBOARD</li>
    <li class="legend__item"><span class="legend__swatch legend__swatch--black"></span>PRINTED BLACK</li>
    <li class="legend__item"><span class="legend__swatch legend__swatch--red"></span>PRINTED RED</li>
  </ul>
</body>
</html>
```